Design a website for a Chocolate Factory (Homepage only, PSD)

Hello, looking for talented designers to re-design an existing website's homepage, with a totally different and elegant approach. Link of website, hires images, some catalog PSD files, logo and website references attached in this google Drive folder:

Sitemap:
-Home (Required to design only)
-About Us
-Catalog (Divided into sub-categories: Chocolate, Cookies, Printed Calisson, Dragees. Bonbon, Malban & Nougat...)
-Contact Us

Good luck :)

```html
<!DOCTYPE html>
<html lang="en">
<head>
<meta charset="utf-8">
<title>Cocoa Lane — Chocolate Factory</title>
<link href="https://fonts.googleapis.com/css2?family=Roboto:wght@300;400;500;700&family=Roboto+Condensed:wght@400;700&family=Open+Sans:wght@400;600;700&family=Alegreya+Sans+SC:wght@500&display=swap" rel="stylesheet">
<style>
:root{
  --cocoa-deep:#2a0f05;
  --cocoa-nav:#3b1a0c;
  --cocoa-hero:#5b3321;
  --cocoa-band:#4a2414;
  --cocoa-text:#4a2618;
  --cream:#f5f5f5;
  --sand:#c9b393;
  --sand-field:#d3bf9f;
  --red:#c0141c;
  --gold:#f2c200;
  --line:#d9d9d9;
  --white:#ffffff;
  --grey-text:#555;
  --map-base:#ebe9e3;
  --map-green:#dfe6d6;
  --map-road:#f6f5f2;
}
*{box-sizing:border-box;margin:0;padding:0}
html,body{width:1200px;height:3025px;overflow:hidden}
body{position:relative;background:var(--cream);font-family:"Open Sans",sans-serif;color:var(--grey-text)}
.abs{position:absolute}

/* header */
.topbar{left:0;top:0;width:1200px;height:27px;background:var(--cocoa-deep);color:#fff;font-size:9px;text-align:right;padding:7px 201px 0 0}
.topbar b{font-weight:700}
.nav{left:0;top:27px;width:1200px;height:64px;background:var(--cocoa-nav)}
.brand{left:120px;top:20px;width:92px;height:92px;border-radius:50%;background:var(--white);display:flex;align-items:center;justify-content:center;font-family:"Roboto",sans-serif;font-weight:700;font-size:15px;color:var(--cocoa-text);z-index:3}
.menu{right:201px;top:49px;display:flex;gap:21px;font-family:"Roboto",sans-serif;font-size:14px;color:#eee;letter-spacing:.3px}
.menu .on{font-weight:700;color:#fff}

/* hero */
.hero{left:0;top:91px;width:1200px;height:440px;background:var(--cocoa-hero)}
.hero-art{left:505px;top:111px;width:540px;height:400px;border-radius:48% 42% 40% 50%;background:radial-gradient(ellipse at 55% 45%,#6e4029 0%,#3d1c0f 60%,rgba(61,28,15,0) 72%)}
.hero-title{left:200px;top:245px;font-family:"Roboto Condensed",sans-serif;color:#fff}
.hero-title h1{font-size:48px;font-weight:700;line-height:1;letter-spacing:.5px}
.hero-title p{font-size:32px;font-weight:400;line-height:1.1;margin-top:4px}
.slide-btn{width:52px;height:48px;display:flex;align-items:center;justify-content:center}
.slide-prev{left:88px;top:270px;background:#c3ab8a}
.slide-next{left:1062px;top:270px;background:var(--cocoa-deep)}
.hero-edge{left:0;top:531px;width:1200px;height:64px;background:linear-gradient(180deg,var(--cocoa-hero) 0%,#8a6a5a 45%,var(--cream) 100%)}

/* section titles */
.sec-title{font-family:"Roboto",sans-serif;color:var(--cocoa-text);display:flex;align-items:center;gap:14px}
.sec-title::after{content:"";flex:1;height:1px;background:var(--line)}
.services-title{left:201px;top:660px;width:796px;font-size:26px;font-weight:400}
.sec-arrows{left:918px;top:665px;display:flex;gap:10px;background:var(--cream);padding-left:6px}
.sec-arrows span{width:26px;height:26px;background:#e2e2e2;display:flex;align-items:center;justify-content:center}

/* service tiles */
.tile{width:250px;height:204px;overflow:hidden}
.tile-photo{width:100%;height:100%}
.tile-label{position:absolute;left:0;bottom:0;width:100%;height:48px;background:rgba(60,30,15,.45);color:#fff;font-family:"Alegreya Sans SC",sans-serif;font-size:22px;text-align:center;line-height:48px}

/* testimonials */
.reviews{left:0;width:1200px;height:260px;background:radial-gradient(circle at 15% 60%,#5a2e1a 0,var(--cocoa-band) 40%,#3a1a0d 100%)}
.reviews h2{position:absolute;left:250px;top:16px;font-family:"Open Sans",sans-serif;font-weight:400;font-size:21px;color:#fff;display:flex;align-items:center;gap:6px}
.reviews h2 b{font-weight:700;color:var(--sand-field)}
.reviews h2::after{content:"";width:70px;height:1px;background:#d9c7ad}
.review{position:absolute;top:92px;height:101px;background:#fff;padding:38px 10px 0 10px}
.review .avatar{position:absolute;left:8px;top:-24px;width:56px;height:56px;background:linear-gradient(#cfa98c,#8d5d43);border:3px solid #fff}
.review .quote{position:absolute;right:18px;top:4px;font-family:"Roboto",sans-serif;font-size:46px;line-height:1;color:#ddd;font-weight:700}
.review .who{font-size:10px;font-weight:700;color:var(--red)}
.review p{font-size:9px;line-height:1.3;color:#333;text-align:justify;margin-top:3px}
.dots{position:absolute;left:577px;top:226px;display:flex;gap:8px}
.dots span{width:10px;height:10px;background:#fff}

/* best seller */
.best-title{left:200px;top:1541px;width:797px;font-size:34px;font-weight:500}
.product{width:250px;height:259px;background:#f8f8f8;border:2px solid #e1e1e1;text-align:center}
.product-photo{margin:30px auto 0;width:140px;height:110px;border-radius:50%}
.product h3{margin-top:22px;font-family:"Alegreya Sans SC",sans-serif;font-weight:500;font-size:22px;color:var(--cocoa-text);line-height:1}
.stars{color:var(--gold);font-size:13px;letter-spacing:3px;margin-top:2px}
.price{font-family:"Open Sans",sans-serif;font-weight:700;font-size:14px;color:#222;margin-top:2px}
.ph-cupcake{background:radial-gradient(ellipse at 50% 35%,#f08ca0 0,#e06f86 45%,#c9596b 70%,rgba(0,0,0,0) 72%)}
.ph-cookies{background:radial-gradient(ellipse at 50% 50%,#d39a57 0,#b57638 55%,rgba(0,0,0,0) 70%)}
.ph-choc{background:radial-gradient(ellipse at 50% 50%,#5e3421 0,#3b1d10 55%,rgba(0,0,0,0) 70%)}

/* contact */
.contact{left:0;top:2489px;width:1200px;height:236px;background:var(--cream)}
.contact-form-bg{left:600px;top:2489px;width:600px;height:236px;background:var(--sand)}
.contact h2{position:absolute;left:252px;top:18px;font-family:"Roboto",sans-serif;font-size:22px;font-weight:400;color:var(--cocoa-text)}
.contact h2 b{color:var(--red);font-weight:700}
.contact-info{position:absolute;left:260px;top:72px;font-size:9px;color:#222;font-weight:600;line-height:1.3}
.contact-info li{list-style:none;display:flex;align-items:center;gap:8px;margin-top:8px}
.social{position:absolute;left:263px;top:185px;display:flex;gap:4px}
.social span{width:21px;height:21px;border-radius:50%;background:var(--cocoa-deep)}
.field{left:632px;width:272px;height:27px;background:var(--sand-field);border:1px solid #e8dcc8;font-size:8px;color:#fff;padding:8px 8px}
.btn-send{left:632px;top:2673px;width:126px;height:28px;background:var(--red);color:#fff;font-size:11px;font-weight:700;text-align:center;line-height:28px;font-family:"Open Sans",sans-serif}

/* map + footer */
.map{left:0;top:2725px;width:1200px;height:282px;background:
  radial-gradient(ellipse at 20% 30%,var(--map-green) 0,rgba(223,230,214,0) 35%),
  radial-gradient(ellipse at 75% 70%,var(--map-green) 0,rgba(223,230,214,0) 30%),
  linear-gradient(160deg,var(--map-road) 0%,var(--map-base) 50%,#e4e2db 100%)}
.footer{left:0;top:3007px;width:1200px;height:18px;background:#1f1f1f;color:#ccc;font-size:8px;text-align:center;line-height:18px}
</style>
</head>
<body>

<header>
  <div class="abs topbar"><b>Call Us Today!</b> 01/555120 | 01/555121 &nbsp;| &nbsp;hello@cocoalane.test</div>
  <div class="abs nav"></div>
  <div class="abs brand">Cocoa Lane</div>
  <nav class="abs menu">
    <span class="on">HOME</span><span>ABOUT</span><span>CATALOG</span><span>CONTACT US</span>
  </nav>
</header>

<section class="hero-section">
  <div class="abs hero"></div>
  <div class="abs hero-art" role="img" aria-label="Pile of assorted chocolates, cupcakes and mango-shaped sweets"></div>
  <div class="abs hero-title">
    <h1>BE HAPPY!</h1>
    <p>EAT CHOCOLATE...</p>
  </div>
  <div class="abs slide-btn slide-prev"><svg width="18" height="30" viewBox="0 0 18 30"><path d="M16 2 3 15l13 13" fill="none" stroke="#fff" stroke-width="2"/></svg></div>
  <div class="abs slide-btn slide-next"><svg width="18" height="30" viewBox="0 0 18 30"><path d="M2 2l13 13L2 28" fill="none" stroke="#fff" stroke-width="2"/></svg></div>
  <div class="abs hero-edge" role="img" aria-label="Melted chocolate dripping edge"></div>
</section>

<section class="services">
  <h2 class="abs sec-title services-title">Our Services</h2>
  <div class="abs sec-arrows">
    <span><svg width="10" height="14"><path d="M8 1 2 7l6 6" fill="none" stroke="#fff" stroke-width="2"/></svg></span>
    <span><svg width="10" height="14"><path d="M2 1l6 6-6 6" fill="none" stroke="#fff" stroke-width="2"/></svg></span>
  </div>

  <div class="abs tile" style="left:201px;top:725px"><div class="tile-photo" role="img" aria-label="Assorted chocolate pralines" style="background:linear-gradient(135deg,#6b3a22,#3a1b0e)"></div><div class="tile-label">Chocolate</div></div>
  <div class="abs tile" style="left:475px;top:725px"><div class="tile-photo" role="img" aria-label="Decorated cake pops" style="background:linear-gradient(135deg,#7da9b4,#4b3a33)"></div><div class="tile-label">Cakepops</div></div>
  <div class="abs tile" style="left:748px;top:725px"><div class="tile-photo" role="img" aria-label="Stacked cream-filled cookies" style="background:linear-gradient(135deg,#b06c35,#3a1a0c)"></div><div class="tile-label">Cookies</div></div>
  <div class="abs tile" style="left:201px;top:956px"><div class="tile-photo" role="img" aria-label="Colourful bonbon candies" style="background:linear-gradient(135deg,#f07a8c,#e9b4b8)"></div><div class="tile-label">Bonbon</div></div>
  <div class="abs tile" style="left:475px;top:956px"><div class="tile-photo" role="img" aria-label="Colourful sugar-coated dragees" style="background:linear-gradient(135deg,#b6477a,#7a5a3c)"></div><div class="tile-label">Dragees</div></div>
  <div class="abs tile" style="left:748px;top:956px"><div class="tile-photo" role="img" aria-label="Frosted cupcakes" style="background:linear-gradient(135deg,#e9b7b5,#6b4a3a)"></div><div class="tile-label">Cupcake</div></div>
</section>

<section class="abs reviews" style="top:1228px">
  <h2><b>Here's what customers</b> are saying about us:</h2>
  <article class="review" style="left:259px;width:308px">
    <div class="avatar" role="img" aria-label="Customer portrait"></div><div class="quote">”</div>
    <div class="who">Mira D.</div>
    <p>Lorem ipsum dolor sit amet, consectetur adipiscing elit. Etiam malesuada condimentum felis, et faucibus diam venenatis interdum. Nullam eros ante, ultricies eget tellus eu, accumsan finibus urna.</p>
  </article>
  <article class="review" style="left:608px;width:325px">
    <div class="avatar" role="img" aria-label="Customer portrait"></div><div class="quote">”</div>
    <div class="who">Nora K.</div>
    <p>Lorem ipsum dolor sit amet, consectetur adipiscing elit. Etiam malesuada condimentum felis, et faucibus diam venenatis interdum. Nullam eros ante, ultricies eget tellus eu, accumsan finibus urna.</p>
  </article>
  <div class="dots"><span></span><span></span><span></span></div>
</section>

<section class="best">
  <h2 class="abs sec-title best-title">BEST SELLER</h2>
  <div class="abs product" style="left:201px;top:1628px"><div class="product-photo ph-cupcake" role="img" aria-label="Pink frosted cupcake"></div><h3>Cuapcake</h3><div class="stars">★★★★★</div><div class="price">5 $</div></div>
  <div class="abs product" style="left:475px;top:1628px"><div class="product-photo ph-cookies" role="img" aria-label="Chocolate chip cookies"></div><h3>Cookies</h3><div class="stars">★★★★★</div><div class="price">15 $</div></div>
  <div class="abs product" style="left:748px;top:1628px"><div class="product-photo ph-choc" role="img" aria-label="Pile of chocolate pieces"></div><h3>Chocolate</h3><div class="stars">★★★★★</div><div class="price">10 $</div></div>
  <div class="abs product" style="left:201px;top:1916px"><div class="product-photo ph-cupcake" role="img" aria-label="Pink frosted cupcake"></div><h3>Cuapcake</h3><div class="stars">★★★★★</div><div class="price">7 $</div></div>
  <div class="abs product" style="left:475px;top:1916px"><div class="product-photo ph-cookies" role="img" aria-label="Chocolate chip cookies"></div><h3>Cookies</h3><div class="stars">★★★★★</div><div class="price">3 $</div></div>
  <div class="abs product" style="left:748px;top:1916px"><div class="product-photo ph-choc" role="img" aria-label="Pile of chocolate pieces"></div><h3>Chocolate</h3><div class="stars">★★★★★</div><div class="price">8 $</div></div>
</section>

<section class="abs reviews" style="top:2229px">
  <h2><b>Here's what customers</b> are saying about us:</h2>
  <article class="review" style="left:259px;width:308px">
    <div class="avatar" role="img" aria-label="Customer portrait"></div><div class="quote">”</div>
    <div class="who">Mira D.</div>
    <p>Lorem ipsum dolor sit amet, consectetur adipiscing elit. Etiam malesuada condimentum felis, et faucibus diam venenatis interdum. Nullam eros ante, ultricies eget tellus eu, accumsan finibus urna.</p>
  </article>
  <article class="review" style="left:608px;width:325px">
    <div class="avatar" role="img" aria-label="Customer portrait"></div><div class="quote">”</div>
    <div class="who">Nora K.</div>
    <p>Lorem ipsum dolor sit amet, consectetur adipiscing elit. Etiam malesuada condimentum felis, et faucibus diam venenatis interdum. Nullam eros ante, ultricies eget tellus eu, accumsan finibus urna.</p>
  </article>
  <div class="dots"><span></span><span></span><span></span></div>
</section>

<section>
  <div class="abs contact">
    <h2><b>Contact</b> Info</h2>
    <ul class="contact-info">
      <li style="display:block;margin-top:0">Cocoa Lane Confectionery Co.<br>12 Orchard Road, Hillside</li>
      <li><svg width="10" height="10" viewBox="0 0 10 10"><path d="M2 0h2l1 3-1.5 1a6 6 0 0 0 2.5 2.5L7 5l3 1v2c0 1-1 2-2 2A8 8 0 0 1 0 2c0-1 1-2 2-2z" fill="#333"/></svg>01/555120 | 01/555121</li>
      <li><svg width="10" height="10" viewBox="0 0 10 10"><rect x="0" y="1" width="10" height="8" fill="#333"/><rect x="2" y="3" width="6" height="2" fill="#fff"/></svg>01/555190</li>
      <li><svg width="10" height="8" viewBox="0 0 10 8"><rect width="10" height="8" fill="#333"/><path d="M0 0l5 4 5-4" fill="none" stroke="#fff"/></svg>hello@cocoalane.test</li>
    </ul>
    <div class="social"><span></span><span></span><span></span></div>
  </div>
  <div class="abs contact-form-bg"></div>
  <div class="abs field" style="top:2502px">Your Name</div>
  <div class="abs field" style="top:2534px">Your E-mail</div>
  <div class="abs field" style="top:2566px">Subject</div>
  <div class="abs field" style="top:2597px;height:61px">Message</div>
  <div class="abs btn-send">SEND A MESSAGE</div>
</section>

<div class="abs map" role="img" aria-label="Street map showing the factory location"></div>
<footer class="abs footer">© Copyright 2018 | All Rights Reserved Cocoa Lane</footer>

</body>
</html>
```